Martin Hale PA Card Logo

Current logo attached. Its 25 year old logo I have used. Looking for a new fresh elegant professional look/design for a law firm that has high net worth clientele and is estate planning business law firm. Firm mis in Palm Beach Florida.
One sided card linen stock white will be used. Logo section name section. Logo should include nice elegant design using the letter "M" perhapa (I am not wed to current font of the M on current logo.) Be creative there with logo design. My initials are MH.......color scheme I figure 3 tone... Raised Gold Foil, Blue name of firm = Martin Hale, P.A. My practice focus is Family and Business Asset Protection. My name is Martin M. Hale, Esq. Practice specialties include Asset Protection trusts, Business Succession Planning, LLC law, Estate Planning, Medicaid Planning (Maybe put those topics in bullets in a section of card. Bottom of card can be reserved smaller print address phone website and email address. Address section is not as important as logo and topics of practice on front. I foresee address section can be in dark blue. MY name and Topics dark blue as well.
Target Market(s)
affluent; business owners executives; wealth 2-10 million net worth
Industry/Entity Type
business law and estate planning
Contact Information for Business Card
White thick linen one sided

```html
<!DOCTYPE html>
<html lang="en">
<head>
<meta charset="utf-8">
<title>Martin Hale, P.A. — Business Card</title>
<link rel="stylesheet" href="https://fonts.googleapis.com/css2?family=Montserrat:wght@600;700;800&family=Open+Sans:wght@400;600&display=swap">
<style>
  :root {
    --navy: #0b2a52;
    --gold: #c19a3e;
    --white: #ffffff;
    --backdrop: #2c2c2e;
    --rule: #0b2a52;
    --ink: #1c2a40;
  }
  * { box-sizing: border-box; margin: 0; padding: 0; }
  html, body { width: 1200px; height: 689px; overflow: hidden; }
  body {
    background: var(--backdrop);
    display: flex;
    align-items: center;
    justify-content: center;
    gap: 36px;
    font-family: "Open Sans", sans-serif;
  }
  .card {
    position: relative;
    width: 548px;
    height: 313px;
    border-radius: 18px;
    overflow: hidden;
  }

  /* Brand mark: plain circle beside the firm name */
  .brand-mark {
    display: flex;
    align-items: center;
    gap: 12px;
    white-space: nowrap;
  }
  .brand-dot {
    flex: none;
    border-radius: 50%;
    background: var(--gold);
  }
  .firm-name {
    font-family: "Montserrat", sans-serif;
    font-weight: 800;
  }

  /* Navy side */
  .card--brand {
    background: var(--navy);
    display: flex;
    align-items: center;
    justify-content: center;
  }
  .card--brand .brand-dot { width: 26px; height: 26px; }
  .card--brand .firm-name { font-size: 30px; color: var(--gold); }

  /* White side */
  .card--details { background: var(--white); }
  .name-band {
    position: absolute;
    left: 0; top: 40px;
    width: 332px; height: 56px;
    background: var(--navy);
    border-radius: 0 28px 28px 0;
    padding: 7px 0 0 26px;
    color: var(--white);
  }
  .attorney-name {
    font-family: "Montserrat", sans-serif;
    font-weight: 700;
    font-size: 20px;
    line-height: 1.2;
  }
  .practice-focus { font-size: 11.5px; line-height: 1.4; }

  .specialties { position: absolute; left: 34px; top: 110px; color: var(--navy); }
  .specialties h2 {
    font-family: "Montserrat", sans-serif;
    font-weight: 800;
    font-size: 14px;
    letter-spacing: 0.3px;
    margin-bottom: 6px;
  }
  .specialties ul { list-style: none; }
  .specialties li {
    font-size: 12.5px;
    line-height: 1.5;
    display: flex;
    align-items: center;
    gap: 8px;
    padding-left: 10px;
    color: var(--ink);
  }
  .specialties li::before {
    content: "";
    width: 7px; height: 7px;
    border: 1.5px solid var(--navy);
    background: radial-gradient(var(--navy) 40%, transparent 45%);
  }

  .card--details .brand-mark {
    position: absolute;
    right: 30px; top: 112px;
    gap: 10px;
  }
  .card--details .brand-dot { width: 20px; height: 20px; }
  .card--details .firm-name { font-size: 22px; color: var(--navy); }

  .contact-rule {
    position: absolute;
    left: 34px; right: 28px; top: 232px;
    border-top: 1.5px solid var(--rule);
  }
  .contact-row {
    position: absolute;
    left: 34px; right: 28px; top: 242px;
    display: flex;
    justify-content: space-between;
    font-size: 12px;
    color: var(--ink);
  }
  .contact-item { display: flex; align-items: center; gap: 5px; }
  .contact-item svg { width: 15px; height: 15px; }

  .address-band {
    position: absolute;
    left: 0; right: 0; bottom: 0;
    height: 36px;
    background: var(--navy);
    color: var(--white);
    font-size: 12px;
    display: flex;
    align-items: center;
    justify-content: center;
    letter-spacing: 0.2px;
  }
</style>
</head>
<body>

  <section class="card card--brand">
    <div class="brand-mark">
      <span class="brand-dot"></span>
      <span class="firm-name">Martin Hale, P.A</span>
    </div>
  </section>

  <section class="card card--details">
    <header class="name-band">
      <div class="attorney-name">Martin M. Hale, Esq.</div>
      <div class="practice-focus">Family and Business Asset Protection</div>
    </header>

    <div class="specialties">
      <h2>PRACTICE SPECIALTIES</h2>
      <ul>
        <li>Asset Protection trusts</li>
        <li>Business Succession Planning</li>
        <li>LLC Law</li>
        <li>Estate Planning</li>
        <li>Medicaid Planning</li>
      </ul>
    </div>

    <div class="brand-mark">
      <span class="brand-dot"></span>
      <span class="firm-name">Martin Hale, P.A</span>
    </div>

    <div class="contact-rule"></div>
    <div class="contact-row">
      <span class="contact-item">
        <svg viewBox="0 0 16 16" aria-hidden="true"><circle cx="8" cy="8" r="7" fill="none" stroke="#0b2a52" stroke-width="1.3"/><path d="M5.3 4.6l1.3-.3.8 1.8-.9.7a5 5 0 0 0 2.6 2.6l.7-.9 1.8.8-.3 1.3c-3.4.3-6.3-2.6-6-6z" fill="#0b2a52"/></svg>
        044-555 018 240
      </span>
      <span class="contact-item">
        <svg viewBox="0 0 16 16" aria-hidden="true"><circle cx="8" cy="8" r="7" fill="none" stroke="#0b2a52" stroke-width="1.3"/><rect x="4" y="5.3" width="8" height="5.4" fill="#0b2a52"/><path d="M4 5.3l4 3 4-3" fill="none" stroke="#fff" stroke-width="0.9"/></svg>
        info@halelawpa.com
      </span>
      <span class="contact-item">
        <svg viewBox="0 0 16 16" aria-hidden="true"><circle cx="8" cy="8" r="7" fill="none" stroke="#0b2a52" stroke-width="1.3"/><circle cx="8" cy="8" r="4.3" fill="none" stroke="#0b2a52"/><ellipse cx="8" cy="8" rx="1.8" ry="4.3" fill="none" stroke="#0b2a52" stroke-width="0.8"/><path d="M3.7 8h8.6" stroke="#0b2a52" stroke-width="0.8"/></svg>
        www.halelawpa.com
      </span>
    </div>

    <footer class="address-band">218, Harbor Lane Suite 4 33480, United States</footer>
  </section>

</body>
</html>
```